Course flyer - evolutive design

We want to have a nice design for our course programm.
In fact we are school language, and our course programm change approximatively each 2 weeks§.
For that we need a design that we can modify each 2 weeks (only dates change ) by ourselves.
We used to have a classical design but we want to upgrade it with a modern and attractive design.
We can have 3 versions one for each city.
We have 3 offices: Tunis, Sousse & Sfax
Attached you can find old designs

Target Market(s)

students from 16 years old till retired people 76 years old

Industry/Entity Type

Education

Font styles to use
Sans Serif

Requirements
Must have
• clear timing for courses (date, days, timing)
• prices
• Adresse (each flyer has its own adress)
• phone Number
• Cool image
Should not have
• Racism
• Violence
• Too much stuff

```html
<!DOCTYPE html>
<html lang="fr">
<head>
<meta charset="utf-8">
<title>Cours d'allemand – Tunis</title>
<link href="https://fonts.googleapis.com/css2?family=Oswald:wght@500;600&family=Titillium+Web:wght@400;600;700&display=swap" rel="stylesheet">
<style>
  :root{
    --red:#e01b22;
    --red-dark:#a3141a;
    --ink:#2a2a2a;
    --band:#333333;
    --yellow:#ffd200;
    --lime:#c8dc1e;
    --white:#ffffff;
    --paper-bg:#e9e9e9;
    --text-font:"Titillium Web", sans-serif;
    --title-font:"Oswald", sans-serif;
  }
  *{box-sizing:border-box;margin:0;padding:0}
  html,body{width:1200px;height:800px;overflow:hidden}
  body{background:radial-gradient(ellipse at 50% 45%, #fafafa 0%, var(--paper-bg) 75%);font-family:var(--text-font)}
  .flyer{position:absolute;left:340px;top:20px;width:520px;height:760px;background:var(--white);overflow:hidden;box-shadow:0 6px 24px rgba(0,0,0,.18)}
  .hero-photo{position:absolute;left:0;top:0;width:520px;height:345px;
    background:linear-gradient(100deg,#e8e4ea 0%,#cfc6d4 30%,#b7a6b9 55%,#3e3d52 78%,#1e2230 100%)}
  .course-title{position:absolute;left:22px;top:40px;font-family:var(--title-font);font-weight:600;font-size:40px;letter-spacing:.5px;color:var(--red);text-transform:uppercase}
  .brand{position:absolute;left:26px;top:160px;display:flex;align-items:center;gap:12px}
  .brand-dot{width:30px;height:30px;border-radius:50%;background:var(--lime)}
  .brand-name{font-family:var(--text-font);font-weight:700;font-size:40px;color:var(--ink);line-height:1}
  .schedule{position:absolute;left:0;width:286px;background:var(--red);color:var(--white);padding:10px 14px}
  .schedule-1{top:345px;height:85px}
  .schedule-2{top:447px;height:83px}
  .schedule-3{top:545px;height:85px}
  .band{position:absolute;left:0;width:286px;background:var(--band)}
  .band-1{top:430px;height:17px}
  .band-2{top:530px;height:15px}
  .band-3{top:630px;height:7px}
  .band-4{top:740px;height:20px;width:286px}
  .course-kind{position:absolute;left:14px;top:8px;font-weight:700;font-size:15px;color:var(--yellow);line-height:1}
  .course-days{position:absolute;left:14px;top:23px;font-weight:700;font-size:10px;line-height:1}
  .course-period{position:absolute;left:132px;top:8px;font-size:9px;line-height:1}
  .slot{position:absolute;top:20px;width:72px;font-size:8px;line-height:11px}
  .slot-am{left:128px}
  .slot-pm{left:200px}
  .slot-time{color:var(--yellow);font-weight:600}
  .slot b{color:var(--yellow);font-weight:700;font-size:9px;margin-right:3px}
  .notes{position:absolute;left:0;top:637px;width:286px;height:103px;background:var(--red);color:var(--white);padding:14px 18px;font-size:8.5px;line-height:12px}
  .price{margin-top:12px;font-weight:700;font-size:9.5px}
  .connectors{position:absolute;left:0;top:0}
  .session-date{position:absolute;left:400px;top:383px;display:flex;align-items:center;gap:6px}
  .months{font-family:var(--title-font);font-weight:500;font-size:22px;line-height:22px;color:var(--red);text-align:right}
  .year{font-family:var(--title-font);font-weight:500;font-size:36px;line-height:32px;color:var(--ink)}
  .students-photo{position:absolute;left:402px;top:462px;width:118px;height:110px;background:linear-gradient(135deg,#b9c3c9,#7d8c96 60%,#4c5964)}
  .city{position:absolute;left:330px;top:700px;transform:rotate(-90deg);transform-origin:left top;font-family:var(--title-font);font-weight:600;font-size:24px;letter-spacing:1px;color:var(--red)}
  .contact{position:absolute;left:362px;top:622px;width:155px;font-style:normal;font-size:8px;line-height:11px;color:var(--ink)}
</style>
</head>
<body>
<main class="flyer">
  <div class="hero-photo" role="img" aria-label="Photo d'une étudiante souriante tenant des cahiers devant une bibliothèque"></div>
  <h1 class="course-title">Course d'allemand</h1>
  <div class="brand"><span class="brand-dot"></span><span class="brand-name">Sprachwerk group</span></div>

  <svg class="connectors" width="520" height="760" viewBox="0 0 520 760" aria-hidden="true">
    <polygon points="286,345 373,462 373,498 286,430" fill="var(--red-dark)"/>
    <polygon points="286,447 373,505 373,540 286,530" fill="var(--red-dark)"/>
    <polygon points="286,545 373,547 373,585 286,630" fill="var(--red-dark)"/>
    <rect x="373" y="462" width="25" height="36" fill="var(--red)"/>
    <rect x="373" y="505" width="25" height="35" fill="var(--red)"/>
    <rect x="373" y="547" width="25" height="38" fill="var(--red)"/>
    <rect x="373" y="590" width="25" height="12" fill="var(--red)"/>
  </svg>

  <section class="schedule schedule-1">
    <span class="course-kind">INTENSIF</span><span class="course-days">(Lundi - Vendredi)</span>
    <span class="course-period">07/03/2016 - 25/03/2016</span>
    <div class="slot slot-am"><div class="slot-time">09H30 - 12H30</div><div><b>A1.1</b>DKS2090</div><div><b>A1.2</b>DKS2091</div><div><b>A2.1</b>DKS2092</div><div><b>A2.2</b>DKS2093</div></div>
    <div class="slot slot-pm"><div class="slot-time">09H30 - 12H30</div><div><b>B1.1</b>DKS2098</div><div><b>B1.2</b>DKS2099</div><div><b>B2.1</b>DKS2094</div></div>
  </section>
  <div class="band band-1"></div>

  <section class="schedule schedule-2">
    <span class="course-kind">EXTENSIF</span><span class="course-days">(Lundi - Vendredi)</span>
    <span class="course-period">07/03/2016 - 25/03/2016</span>
    <div class="slot slot-am"><div class="slot-time">09H30 - 12H30</div><div><b>A1.1</b>DKS2090</div><div><b>A1.2</b>DKS2091</div><div><b>A2.1</b>DKS2092</div><div><b>A2.2</b>DKS2093</div></div>
    <div class="slot slot-pm"><div class="slot-time">09H30 - 12H30</div><div><b>B1.1</b>DKS2098</div><div><b>B1.2</b>DKS2099</div><div><b>B2.1</b>DKS2094</div></div>
  </section>
  <div class="band band-2"></div>

  <section class="schedule schedule-3">
    <span class="course-kind">INTENSIF</span><span class="course-days">(Lundi - Vendredi)</span>
    <span class="course-period">07/03/2016 - 25/03/2016</span>
    <div class="slot slot-am"><div class="slot-time">09H30 - 12H30</div><div><b>A1.1</b>DKS2090</div><div><b>A1.2</b>DKS2091</div><div><b>A2.1</b>DKS2092</div><div><b>A2.2</b>DKS2093</div></div>
    <div class="slot slot-pm"><div class="slot-time">09H30 - 12H30</div><div><b>B1.1</b>DKS2098</div><div><b>B1.2</b>DKS2099</div><div><b>B2.1</b>DKS2094</div></div>
  </section>
  <div class="band band-3"></div>

  <section class="notes">
    <p>Toute inscription doit impérativement se faire au plus tard une semaine avant le début de course.</p>
    <p>Nombre minimum de 4 participants requis.</p>
    <p>L'horaire de course est susceptible d'être modifié.</p>
    <p class="price">Prix par Module 340 TND.</p>
  </section>
  <div class="band band-4"></div>

  <div class="session-date">
    <div class="months">MARS<br>AVRIL</div>
    <div class="year">20<br>16</div>
  </div>
  <div class="students-photo" role="img" aria-label="Photo d'un groupe d'étudiants travaillant ensemble sur un ordinateur portable"></div>

  <div class="city">TUNIS</div>
  <address class="contact">
    Imm. Les Amandiers, 3ème étage 8 Rue des Jasmins (en face du Parc Horizon)<br>
    2045 Cité des Pins<br>
    Tél : +216 71 000 482<br>
    tunis@sprachwerk-langues.org<br>
    www.sprachwerk-langues.org<br>
    www.sprachwerk-langues.org/actus
  </address>
</main>
</body>
</html>
```